Corporate Stationary for Beverage Alcohol Company
Brook Harbor Global Ltd. Co.
Corporate Stationary for Beverage Alcohol Company - Beverages
Creative Brief
Corporate
Dean Walter Prosser
President
512 Fenwood Drive Richmond, KY 40475
dean.prosser@brook-harbor.com
www.brook-harbor.com
The stationary shall be cutting edge and will utilize the logo art work. I would like an abstract border included on the side(s) of the letterhead, envelope and the business card.
Company Name Logo Abstract border

```html
<!DOCTYPE html>
<html lang="en">
<head>
<meta charset="utf-8">
<title>Brook Harbor Global Ltd. Co. – Business Cards</title>
<link href="https://fonts.googleapis.com/css2?family=Crimson+Text:wght@400;600;700&display=swap" rel="stylesheet">
<style>
  :root {
    --backdrop: #2b2b2d;
    --card: #ffffff;
    --ink: #2a2a2a;
    --muted: #555555;
    --gold: #c8932a;
    --gold-light: #f1d27a;
    --gold-dark: #8a5f14;
    --rule: #c9c9c9;
  }
  * { box-sizing: border-box; margin: 0; padding: 0; }
  html, body { width: 1200px; height: 852px; overflow: hidden; }
  body {
    background: var(--backdrop);
    font-family: "Crimson Text", Georgia, serif;
    color: var(--ink);
    position: relative;
  }
  .card {
    position: absolute;
    width: 500px;
    height: 290px;
    background: var(--card);
    border-radius: 14px;
    overflow: hidden;
    box-shadow: 0 10px 24px rgba(0,0,0,.45);
  }
  .card--front { left: 60px; top: 281px; }
  .card--back  { left: 640px; top: 281px; }
  .gold-band {
    position: absolute; left: 0; right: 0; bottom: 0; height: 30px;
    background: linear-gradient(90deg, var(--gold-dark), var(--gold-light) 35%, var(--gold) 60%, var(--gold-light) 80%, var(--gold-dark));
  }
  .brand { display: flex; flex-direction: column; align-items: center; gap: 8px; }
  .brand__dot {
    width: 44px; height: 44px; border-radius: 50%;
    background: var(--gold);
  }
  .brand__name {
    font-size: 19px; font-weight: 600; letter-spacing: .5px;
    color: var(--ink); white-space: nowrap;
  }
  .card--front .brand { position: absolute; top: 34px; left: 0; right: 0; }
  .person__name { color: var(--gold); font-size: 21px; font-weight: 600; line-height: 1.1; white-space: nowrap; }
  .person__title { font-size: 14px; font-weight: 600; color: var(--ink); margin-top: 4px; }
  .divider { position: absolute; width: 1px; background: var(--rule); }
  .contact { font-size: 13px; color: var(--muted); line-height: 1.35; white-space: nowrap; }
  .contact__row { display: flex; align-items: center; gap: 7px; margin-top: 4px; }
  .contact__row svg { width: 12px; height: 12px; flex: none; }
  .card--front .person { position: absolute; left: 40px; top: 170px; text-align: right; width: 185px; }
  .card--front .divider { left: 245px; top: 160px; height: 82px; }
  .card--front .contact { position: absolute; left: 262px; top: 160px; }
  .card--back .brand { position: absolute; left: 24px; top: 82px; width: 200px; }
  .card--back .brand__name { font-size: 16px; }
  .card--back .divider { left: 238px; top: 40px; height: 190px; }
  .card--back .person { position: absolute; left: 256px; top: 44px; }
  .card--back .contact { position: absolute; left: 256px; top: 108px; }
  .card--back .contact__row--first { margin-top: 12px; }
</style>
</head>
<body>

<section class="card card--front">
  <div class="brand">
    <span class="brand__dot"></span>
    <span class="brand__name">Brook Harbor Global Ltd. Co.</span>
  </div>
  <div class="person">
    <div class="person__name">Dean Walter Prosser</div>
    <div class="person__title">President</div>
  </div>
  <span class="divider"></span>
  <div class="contact">
    <div>512 Fenwood Drive<br>Ashford, TN 37012</div>
    <div class="contact__row">
      <svg viewBox="0 0 12 12"><path d="M3 1l2 2.5-1.2 1.2a7 7 0 0 0 3.5 3.5L8.5 7 11 9l-1.5 2A9 9 0 0 1 1 2.5z" fill="#c8932a"/></svg>
      (555) 214-7730
    </div>
    <div class="contact__row">
      <svg viewBox="0 0 12 12"><rect x="1" y="2.5" width="10" height="7" rx="1" fill="none" stroke="#c8932a" stroke-width="1.3"/><path d="M1.5 3l4.5 3.5L10.5 3" fill="none" stroke="#c8932a" stroke-width="1.2"/></svg>
      dean.prosser@brook-harbor.com
    </div>
  </div>
  <div class="gold-band"></div>
</section>

<section class="card card--back">
  <div class="brand">
    <span class="brand__dot"></span>
    <span class="brand__name">Brook Harbor Global Ltd. Co.</span>
  </div>
  <span class="divider"></span>
  <div class="person">
    <div class="person__name">Dean Walter Prosser</div>
    <div class="person__title">President</div>
  </div>
  <div class="contact">
    <div>512 Fenwood Drive<br>Ashford, TN 37012</div>
    <div class="contact__row contact__row--first">
      <svg viewBox="0 0 12 12"><path d="M3 1l2 2.5-1.2 1.2a7 7 0 0 0 3.5 3.5L8.5 7 11 9l-1.5 2A9 9 0 0 1 1 2.5z" fill="#c8932a"/></svg>
      (555) 214-7730
    </div>
    <div class="contact__row">
      <svg viewBox="0 0 12 12"><rect x="1" y="2.5" width="10" height="7" rx="1" fill="none" stroke="#c8932a" stroke-width="1.3"/><path d="M1.5 3l4.5 3.5L10.5 3" fill="none" stroke="#c8932a" stroke-width="1.2"/></svg>
      dean.prosser@brook-harbor.com
    </div>
    <div class="contact__row">
      <svg viewBox="0 0 12 12"><circle cx="6" cy="6" r="4.8" fill="none" stroke="#c8932a" stroke-width="1.2"/><path d="M1.2 6h9.6M6 1.2c-2.4 2.6-2.4 7 0 9.6M6 1.2c2.4 2.6 2.4 7 0 9.6" fill="none" stroke="#c8932a" stroke-width="1"/></svg>
      www.brook-harbor.com
    </div>
  </div>
  <div class="gold-band"></div>
</section>

</body>
</html>
```